Tour agency for FIT and groups need a business card design

We need a business card design for a tour agency company that is based in Perth called" BRISK NO", we aim to provide customise, unique and seamless travel arrangement for FIT and groups. We serve both high profile businessperson, government authorities, business partners, executives and investors. The name card should be more professional looking.
Updates

Project Deadline Extended Reason: Have some changes that needed to make, director will be back to office on Monday, sorry for the inconvenience cause. Added Saturday, May 6, 2017

Target Market(s)

High profile businessperson, government authorities, business partners, executives and investors.

Industry/Entity Type

Tourism

Contact Information for Business Card

Brisk NO
Level 1, 214 Marlowe Avenue, Dunreath NO, 6120
www.briskno.com.au

Font styles to use
Serif

Colors

Designer to choose colors to be used in the design.

Requirements
Must have
• My project must have a company logo
Nice to have
• a more professional and solid yet friendly name card design. We may want to include chinese name in the name card as well. Edge of the card can be filled with gold and we think that transparent name cards are interesting.

```html
<!DOCTYPE html>
<html lang="en">
<head>
<meta charset="utf-8">
<title>Brisk NO — Business Card</title>
<link rel="stylesheet" href="https://fonts.googleapis.com/css2?family=Ubuntu:wght@400;500&display=swap">
<style>
  :root {
    --brand-blue: #00aadb;
    --paper: #ffffff;
    --ink: #333333;
    --ink-soft: #444444;
    --rule: #9a9a9a;
    --backdrop: #eeeeee;
  }
  * { margin: 0; padding: 0; box-sizing: border-box; }
  html, body {
    width: 1200px;
    height: 1200px;
    overflow: hidden;
    background: var(--backdrop);
    font-family: "Ubuntu", sans-serif;
  }
  .canvas {
    width: 1200px;
    height: 1200px;
    display: flex;
    flex-direction: column;
    align-items: center;
    justify-content: center;
    gap: 50px;
  }
  .card {
    width: 860px;
    height: 526px;
    position: relative;
    box-shadow: 0 4px 16px rgba(0, 0, 0, 0.12);
  }
  .card--front {
    background: var(--brand-blue);
    display: flex;
    align-items: center;
    justify-content: center;
  }
  .wordmark {
    font-weight: 500;
    letter-spacing: 1px;
    white-space: nowrap;
  }
  .card--front .wordmark {
    color: var(--paper);
    font-size: 84px;
  }
  .card--back {
    background: var(--paper);
  }
  .card--back .wordmark {
    position: absolute;
    left: 70px;
    top: 226px;
    color: var(--brand-blue);
    font-size: 56px;
  }
  .contact-block {
    position: absolute;
    left: 430px;
    top: 190px;
    width: 370px;
  }
  .person-name {
    color: var(--ink);
    font-size: 36px;
    font-weight: 400;
    line-height: 1.1;
  }
  .person-role {
    color: var(--brand-blue);
    font-size: 23px;
    margin-top: 8px;
    padding-bottom: 10px;
    border-bottom: 1.5px solid var(--rule);
  }
  .contact-list {
    list-style: none;
    margin-top: 20px;
  }
  .contact-item {
    display: flex;
    align-items: flex-start;
    gap: 14px;
    color: var(--ink-soft);
    font-size: 20px;
    line-height: 1.35;
    margin-bottom: 13px;
  }
  .contact-icon {
    flex: 0 0 22px;
    width: 22px;
    height: 22px;
    margin-top: 2px;
    fill: var(--brand-blue);
  }
</style>
</head>
<body>
<main class="canvas">
  <section class="card card--front" aria-label="Card front">
    <span class="wordmark">Brisk NO</span>
  </section>

  <section class="card card--back" aria-label="Card back">
    <span class="wordmark">Brisk NO</span>
    <div class="contact-block">
      <h1 class="person-name">Marcus Lowe</h1>
      <p class="person-role">Accountant</p>
      <ul class="contact-list">
        <li class="contact-item">
          <svg class="contact-icon" viewBox="0 0 24 24" aria-hidden="true"><path d="M12 1C7.6 1 4.5 4.2 4.5 8.4 4.5 14 12 23 12 23s7.5-9 7.5-14.6C19.5 4.2 16.4 1 12 1zm0 10.4a3 3 0 1 1 0-6 3 3 0 0 1 0 6z"/></svg>
          <span>Level 1, 214 Marlowe Avenue,<br>Dunreath NO, 6120</span>
        </li>
        <li class="contact-item">
          <svg class="contact-icon" viewBox="0 0 24 24" aria-hidden="true"><path d="M1 5h22v14H1z" fill="none"/><path d="M1 5h22v2l-11 7L1 7zM1 9l11 7 11-7v10H1z"/></svg>
          <span>hello@briskno.com.au</span>
        </li>
        <li class="contact-item">
          <svg class="contact-icon" viewBox="0 0 24 24" aria-hidden="true"><path d="M7 1h10a1.5 1.5 0 0 1 1.5 1.5v19A1.5 1.5 0 0 1 17 23H7a1.5 1.5 0 0 1-1.5-1.5v-19A1.5 1.5 0 0 1 7 1zm0.8 3v14h8.4V4zM12 19.2a1.2 1.2 0 1 0 0 2.4 1.2 1.2 0 0 0 0-2.4z"/></svg>
          <span>08 61473520</span>
        </li>
        <li class="contact-item">
          <svg class="contact-icon" viewBox="0 0 24 24" aria-hidden="true"><path d="M12 1a11 11 0 1 0 0 22 11 11 0 0 0 0-22zm0 2c1.3 1.4 2.2 3.6 2.5 6h-5c.3-2.4 1.2-4.6 2.5-6zM9.4 3.4C8.4 5 7.7 6.9 7.5 9H3.3a9 9 0 0 1 6.1-5.6zm5.2 0A9 9 0 0 1 20.7 9h-4.2c-.2-2.1-.9-4-1.9-5.6zM3.1 11h4.3v2H3.1zm6.4 0h5v2h-5zm7.1 0h4.3v2h-4.3zM3.3 15h4.2c.2 2.1.9 4 1.9 5.6A9 9 0 0 1 3.3 15zm6.2 0h5c-.3 2.4-1.2 4.6-2.5 6-1.3-1.4-2.2-3.6-2.5-6zm7 0h4.2a9 9 0 0 1-6.1 5.6c1-1.6 1.7-3.5 1.9-5.6z"/></svg>
          <span>www.briskno.com.au</span>
        </li>
      </ul>
    </div>
  </section>
</main>
</body>
</html>
```